Physiotherapy Referral Pad

-Need a referral pad for physiotherapy to be provided to doctors' offices. I would like it to be simple, not too cluttered and sharp looking so doctors can quickly complete it for clients.

-I have attached my logo which I would like to include. I have also included my business cards to keep the style, font, colors etc consistent.

-I would like to include my slogan
From Our Home To Yours

-I would like it to include services options with tick boxes for Mobile, Clinic, Telehealth, NPKRTW

-I would like for it to say Call to Book or Book Online

-I would like it to include my clinic address:
742 Larkin Crescent
Whitehorse, YT
Y1B2K9

-I would like it to include my contact info:
Gavin Trusk BSc(kin), MPT, CAFCI, IMS
(867)555-0142
physio@trusktherapy.ca

-I would like lines for the following:
Patient Name:
Diagnosis/Recommendations:
(extra lines to fill out patient info)

Physician Signature
Date

Target Market(s)

Physicians to refer clients to physiotherapy

Industry/Entity Type

Physical Therapy

Requirements
Must have
• Clean, concise, easy to look at and find pertinant categories for physicians
Nice to have
• Trusk Therapy color scheme. Please see business cards and website as needed
Should not have
• Not too cluttered or wordy

```html
<!DOCTYPE html>
<html lang="en">
<head>
<meta charset="utf-8">
<title>Trusk Therapy Physiotherapy Referral Pad – ver 1</title>
<link href="https://fonts.googleapis.com/css2?family=Poppins:wght@400;500;600;700&family=Roboto+Condensed:wght@400&family=Open+Sans:wght@400&display=swap" rel="stylesheet">
<style>
  :root {
    --navy: #2c4674;
    --green: #03524a;
    --brand-green: #06594c;
    --ink: #222a33;
    --label: #3a4048;
    --muted: #7a7a7a;
    --rule: #a9adb3;
    --backdrop: #ececec;
    --paper: #ffffff;
  }
  * { margin: 0; padding: 0; box-sizing: border-box; }
  html, body { width: 858px; height: 1200px; overflow: hidden; }
  body { background: var(--backdrop); font-family: "Poppins", sans-serif; position: relative; }

  .version-title {
    position: absolute; top: 30px; left: 0; width: 858px; text-align: center;
    font-family: "Roboto Condensed", sans-serif; font-weight: 400;
    font-size: 36px; color: var(--navy);
  }

  .sheet {
    position: absolute; left: 52px; top: 88px; width: 756px; height: 1066px;
    background: var(--paper); box-shadow: 0 2px 14px rgba(0,0,0,.18);
  }
  .top-rule { position: absolute; left: 0; top: 0; width: 100%; height: 7px; background: var(--navy); }

  /* Brand */
  .brand { position: absolute; left: 54px; top: 66px; display: flex; align-items: center; gap: 10px; }
  .brand-mark { width: 26px; height: 26px; background: var(--navy); }
  .brand-name { font-size: 24px; font-weight: 700; color: var(--brand-green); letter-spacing: .4px; }

  /* Contact column */
  .contact { position: absolute; right: 11px; top: 15px; }
  .contact-row { display: flex; justify-content: flex-end; align-items: center; gap: 11px; height: 30px; margin-bottom: 10px; }
  .contact-text { text-align: right; font-size: 11.5px; line-height: 15px; color: #444; }
  .contact-icon { width: 30px; height: 30px; border-radius: 4px; display: flex; align-items: center; justify-content: center; }
  .contact-icon.green { background: var(--green); }
  .contact-icon.navy { background: var(--navy); }

  /* Practitioner block */
  .practitioner { position: absolute; left: 52px; top: 186px; color: var(--ink); }
  .practitioner-from { font-size: 14px; line-height: 20px; }
  .practitioner-name { font-size: 21px; font-weight: 700; color: var(--navy); line-height: 28px; letter-spacing: .3px; }
  .practitioner-creds, .practitioner-role { font-size: 14px; line-height: 21px; }

  .referral-date { position: absolute; right: 33px; top: 254px; font-size: 14px; color: var(--ink); display: flex; align-items: flex-end; gap: 6px; }
  .referral-date b { color: var(--navy); font-weight: 600; }
  .referral-date .blank { width: 110px; border-bottom: 1px solid var(--rule); height: 18px; }

  /* Referral form */
  .referral-form { position: absolute; left: 52px; top: 322px; width: 672px; color: var(--label); font-size: 13px; }
  .slogan { font-size: 15px; font-weight: 600; color: var(--navy); letter-spacing: .3px; margin-bottom: 18px; }
  .slogan span { color: var(--brand-green); }

  .field { display: flex; align-items: flex-end; gap: 8px; height: 34px; }
  .field-label { white-space: nowrap; font-weight: 500; color: var(--label); }
  .field-line { flex: 1; border-bottom: 1px solid var(--rule); height: 18px; }
  .field-pair { display: flex; gap: 28px; }
  .field-pair .field { flex: 1; }

  .services { display: flex; align-items: center; gap: 30px; margin-top: 22px; height: 24px; }
  .services-label { font-weight: 600; color: var(--navy); }
  .service-option { display: flex; align-items: center; gap: 8px; }
  .tick-box { width: 14px; height: 14px; border: 1.5px solid var(--navy); border-radius: 2px; }

  .diagnosis { margin-top: 22px; }
  .diagnosis-label { font-weight: 600; color: var(--navy); }
  .write-line { border-bottom: 1px solid var(--rule); height: 32px; }

  /* Sign-off */
  .signature-rule { position: absolute; left: 52px; top: 902px; width: 220px; height: 2px; background: var(--ink); }
  .signature-label, .date-label {
    position: absolute; top: 910px; text-align: center;
    font-family: "Open Sans", sans-serif; font-size: 13px; letter-spacing: 3px; color: #666;
  }
  .signature-label { left: 52px; width: 220px; }
  .date-rule { position: absolute; right: 33px; top: 902px; width: 160px; height: 2px; background: var(--ink); }
  .date-label { right: 33px; width: 160px; }

  /* Footer band */
  .footer { position: absolute; left: 0; bottom: 0; width: 756px; height: 41px; }
  .footer svg { position: absolute; left: 0; top: 0; }
  .booking { position: absolute; left: 52px; top: 12px; font-size: 11px; color: #fff; }
  .booking b, .page-no b { font-weight: 600; }
  .page-no { position: absolute; right: 11px; top: 12px; font-size: 11px; color: #fff; }
</style>
</head>
<body>
  <h1 class="version-title">PAD- ver 1</h1>

  <main class="sheet">
    <div class="top-rule"></div>

    <div class="brand">
      <span class="brand-mark"></span>
      <span class="brand-name">Trusk Therapy</span>
    </div>

    <div class="contact">
      <div class="contact-row">
        <div class="contact-text">(867)555-0142<br>Call to Book</div>
        <div class="contact-icon green">
          <svg width="14" height="14" viewBox="0 0 24 24"><path fill="#fff" d="M6.6 10.8a15.1 15.1 0 0 0 6.6 6.6l2.2-2.2a1 1 0 0 1 1-.25 11.4 11.4 0 0 0 3.6.57 1 1 0 0 1 1 1V20a1 1 0 0 1-1 1A17 17 0 0 1 3 4a1 1 0 0 1 1-1h3.5a1 1 0 0 1 1 1c0 1.25.2 2.45.57 3.57a1 1 0 0 1-.25 1z"/></svg>
        </div>
      </div>
      <div class="contact-row">
        <div class="contact-text">physio@trusktherapy.ca<br>www.trusktherapy.ca</div>
        <div class="contact-icon navy">
          <svg width="14" height="11" viewBox="0 0 24 18"><path fill="#fff" d="M0 2a2 2 0 0 1 2-2h20a2 2 0 0 1 2 2v.6l-12 7.4L0 2.6z M0 5l12 7.4L24 5v11a2 2 0 0 1-2 2H2a2 2 0 0 1-2-2z"/></svg>
        </div>
      </div>
      <div class="contact-row">
        <div class="contact-text">742 Larkin Crescent<br>Whitehorse, YT Y1B2K9</div>
        <div class="contact-icon green">
          <svg width="11" height="15" viewBox="0 0 16 22"><path fill="#fff" d="M8 0a8 8 0 0 0-8 8c0 6 8 14 8 14s8-8 8-14a8 8 0 0 0-8-8zm0 11a3 3 0 1 1 0-6 3 3 0 0 1 0 6z"/></svg>
        </div>
      </div>
    </div>

    <section class="practitioner">
      <div class="practitioner-from">Refer To</div>
      <div class="practitioner-name">Gavin Trusk</div>
      <div class="practitioner-creds">BSc(kin), MPT, CAFCI, IMS</div>
      <div class="practitioner-role">Physiotherapy Referral</div>
    </section>

    <div class="referral-date"><b>Date:</b><span class="blank"></span></div>

    <section class="referral-form">
      <p class="slogan">From Our Home <span>To Yours</span></p>

      <div class="field"><span class="field-label">Patient Name:</span><span class="field-line"></span></div>
      <div class="field-pair">
        <div class="field"><span class="field-label">Date of Birth:</span><span class="field-line"></span></div>
        <div class="field"><span class="field-label">Phone:</span><span class="field-line"></span></div>
      </div>
      <div class="field"><span class="field-label">Address:</span><span class="field-line"></span></div>
      <div class="field"><span class="field-label">Health Card No:</span><span class="field-line"></span></div>

      <div class="services">
        <span class="services-label">Services:</span>
        <label class="service-option"><span class="tick-box"></span>Mobile</label>
        <label class="service-option"><span class="tick-box"></span>Clinic</label>
        <label class="service-option"><span class="tick-box"></span>Telehealth</label>
        <label class="service-option"><span class="tick-box"></span>NPKRTW</label>
      </div>

      <div class="diagnosis">
        <p class="diagnosis-label">Diagnosis/Recommendations:</p>
        <div class="write-line"></div>
        <div class="write-line"></div>
        <div class="write-line"></div>
        <div class="write-line"></div>
        <div class="write-line"></div>
        <div class="write-line"></div>
      </div>
    </section>

    <div class="signature-rule"></div>
    <div class="signature-label">[PHYSICIAN SIGNATURE]</div>
    <div class="date-rule"></div>
    <div class="date-label">[DATE]</div>

    <footer class="footer">
      <svg width="756" height="41" viewBox="0 0 756 41">
        <rect width="756" height="41" fill="var(--navy)"/>
        <polygon points="0,0 669,0 680,20.5 669,41 0,41" fill="var(--green)"/>
        <polyline points="675,0 686,20.5 675,41" fill="none" stroke="#fff" stroke-width="3"/>
      </svg>
      <div class="booking"><b>Call to Book or Book Online:</b> (867)555-0142 · www.trusktherapy.ca</div>
      <div class="page-no"><b>Page:</b> 01</div>
    </footer>
  </main>
</body>
</html>
```